11 x 17 Orvanthes Quote

Design the following quote in a poster.

"First say to yourself what you would be; then do what you have to do." - Orvanthes

See here for inspiration - https://prints.mornbrekal.com/

Quote

```html
<!DOCTYPE html>
<html lang="en">
<head>
<meta charset="utf-8">
<title>Orvanthes Quote Poster</title>
<link href="https://fonts.googleapis.com/css2?family=Rubik+Wet+Paint&family=Outfit:wght@600;800&display=swap" rel="stylesheet">
<style>
  :root {
    --paper: #ddd6c3;
    --paper-light: #e4ddcb;
    --paper-dark: #d3cbb6;
    --ink: #1f2b2e;
    --quote-mark: #a9a498;
    --byline: #5e5f61;
    --fold: rgba(255, 255, 255, 0.28);
  }
  html, body {
    margin: 0;
    padding: 0;
    width: 848px;
    height: 1200px;
    overflow: hidden;
    background: var(--paper);
  }
  .poster {
    position: relative;
    width: 848px;
    height: 1200px;
    overflow: hidden;
    background:
      radial-gradient(ellipse at 30% 25%, var(--paper-light) 0%, transparent 60%),
      radial-gradient(ellipse at 75% 80%, var(--paper-dark) 0%, transparent 65%),
      var(--paper);
  }
  .paper-texture {
    position: absolute;
    inset: 0;
  }
  .fold {
    position: absolute;
    background: var(--fold);
  }
  .fold--vertical { left: 424px; top: 0; width: 1px; height: 1200px; }
  .fold--upper { left: 0; top: 400px; width: 848px; height: 1px; }
  .fold--lower { left: 0; top: 940px; width: 848px; height: 1px; }

  .quote-mark {
    position: absolute;
    font-family: "Outfit", sans-serif;
    font-weight: 800;
    font-size: 360px;
    line-height: 1;
    color: var(--quote-mark);
    margin: 0;
  }
  .quote-mark--open { left: 14px; top: 158px; }
  .quote-mark--close { left: 520px; top: 836px; }

  .quote {
    position: absolute;
    left: 0;
    top: 0;
    width: 848px;
    margin: 0;
    font-family: "Rubik Wet Paint", sans-serif;
    font-size: 58px;
    color: var(--ink);
    text-align: center;
  }
  .quote__line {
    position: absolute;
    left: 0;
    width: 848px;
    line-height: 1;
    white-space: nowrap;
  }
  .quote__line:nth-child(1) { top: 258px; }
  .quote__line:nth-child(2) { top: 345px; }
  .quote__line:nth-child(3) { top: 430px; }
  .quote__line:nth-child(4) { top: 515px; }
  .quote__line:nth-child(5) { top: 598px; }
  .quote__line:nth-child(6) { top: 683px; }
  .quote__line:nth-child(7) { top: 766px; }
  .quote__line:nth-child(8) { top: 850px; }

  .byline {
    position: absolute;
    right: 51px;
    top: 1054px;
    margin: 0;
    font-family: "Outfit", sans-serif;
    font-weight: 600;
    font-size: 34px;
    color: var(--byline);
    letter-spacing: 0.5px;
  }
</style>
</head>
<body>
  <main class="poster">
    <div class="paper-texture" role="img" aria-label="Worn, scratched beige paper texture"></div>
    <span class="fold fold--vertical"></span>
    <span class="fold fold--upper"></span>
    <span class="fold fold--lower"></span>

    <span class="quote-mark quote-mark--open" aria-hidden="true">&ldquo;</span>

    <blockquote class="quote">
      <span class="quote__line">FIRST SAY</span>
      <span class="quote__line">TO YOUR</span>
      <span class="quote__line">SELF WHAT</span>
      <span class="quote__line">YOU WOULD</span>
      <span class="quote__line">BE; THEN</span>
      <span class="quote__line">DO WHAT</span>
      <span class="quote__line">YOU HAVE</span>
      <span class="quote__line">TO DO.</span>
    </blockquote>

    <span class="quote-mark quote-mark--close" aria-hidden="true">&rdquo;</span>

    <p class="byline">&ndash; Orvanthes</p>
  </main>
</body>
</html>
```